I would like a business card to match my truck wrap and logo. I would like the font to match my existing business card please.

Industry/Entity Type

Painter

Contact Information for Business Card

Rodrigo Venaza 801-437-2916 Venazacoatings.utah@brushmail.net
SERVICES - Custom Paint & Stain, Interior & Exterior, Epoxy Coatings / Garage Floors, Cabinet Refinishing, Log Staining and Refinishing.

Requirements
Nice to have
• I would like to have the white and grey line like the bottom of my vehicle wrap, Light Grey to match my truck also.

```html
<!DOCTYPE html>
<html lang="en">
<head>
<meta charset="utf-8">
<title>Venaza Coatings – Business Card</title>
<link rel="stylesheet" href="https://fonts.googleapis.com/css2?family=Montserrat:wght@400;500;700;800&family=Roboto:wght@400;500&display=swap">
<style>
  :root {
    --page-bg: #e9eaec;
    --card-dark: #3b3c3e;
    --card-dark-edge: #2f3032;
    --card-light: #ffffff;
    --brand-blue: #1aa3e6;
    --ink: #4a4a4c;
    --ink-on-dark: #f4f5f6;
    --watermark: #e4f0f8;
  }
  * { box-sizing: border-box; margin: 0; padding: 0; }
  html, body {
    width: 1200px; height: 881px; overflow: hidden;
    background: var(--page-bg);
    font-family: "Montserrat", Arial, sans-serif;
  }
  .sheet { position: relative; width: 1200px; height: 881px; }
  .card {
    position: absolute; left: 320px;
    width: 560px; height: 320px;
    border-radius: 18px;
    overflow: hidden;
    box-shadow: 0 10px 28px rgba(0,0,0,.18);
  }

  /* ---------- Back side ---------- */
  .card-back {
    top: 60px;
    background: linear-gradient(160deg, var(--card-dark) 0%, var(--card-dark-edge) 100%);
    color: var(--ink-on-dark);
    text-align: center;
  }
  .brand { display: flex; align-items: center; gap: 14px; }
  .brand-mark { width: 26px; height: 26px; border-radius: 4px; background: var(--brand-blue); }
  .brand-name {
    font-family: "Montserrat", Arial, sans-serif;
    font-weight: 800; color: var(--brand-blue);
    text-transform: uppercase; letter-spacing: 2px; line-height: 1;
  }
  .card-back .brand { position: absolute; top: 78px; left: 0; right: 0; justify-content: center; }
  .card-back .brand-mark { width: 44px; height: 44px; border-radius: 6px; }
  .card-back .brand-name { font-size: 36px; }
  .services { position: absolute; left: 30px; right: 30px; top: 170px; }
  .services-title {
    font-weight: 500; font-size: 17px; letter-spacing: 1px;
    color: var(--brand-blue); margin-bottom: 10px;
  }
  .services-list {
    font-family: "Roboto", Arial, sans-serif;
    font-size: 14.5px; line-height: 1.6; color: var(--ink-on-dark);
  }
  .services-list .sep { color: var(--brand-blue); padding: 0 4px; }

  /* ---------- Front side ---------- */
  .card-front { top: 480px; background: var(--card-light); color: var(--ink); }
  .card-front .brand { position: absolute; top: 30px; right: 36px; }
  .card-front .brand-mark { width: 30px; height: 30px; }
  .card-front .brand-name { font-size: 24px; }
  .faint-mark {
    position: absolute; right: 40px; top: 96px;
    width: 180px; height: 180px; border-radius: 14px;
    background: var(--watermark);
  }
  .accent-bar {
    position: absolute; left: 0; top: 134px;
    width: 10px; height: 44px; background: var(--brand-blue);
  }
  .holder { position: absolute; left: 36px; right: 36px; top: 126px; }
  .holder-name {
    font-weight: 500; font-size: 26px; letter-spacing: 1px;
    color: var(--brand-blue); text-transform: uppercase; line-height: 1.1;
  }
  .holder-title { font-family: "Roboto", Arial, sans-serif; font-size: 15px; color: var(--ink); margin-top: 2px; }
  .holder-rule { width: 100%; height: 1px; background: var(--brand-blue); margin: 10px 0 12px; }
  .contact-list { list-style: none; }
  .contact-list li {
    display: flex; align-items: center; gap: 8px;
    font-family: "Roboto", Arial, sans-serif;
    font-size: 14.5px; color: var(--ink); line-height: 1.5;
  }
  .contact-list svg { width: 12px; height: 12px; flex: none; }
</style>
</head>
<body>
<main class="sheet">

  <section class="card card-back" aria-label="Card back">
    <div class="brand">
      <span class="brand-mark"></span>
      <span class="brand-name">Venaza Coatings</span>
    </div>
    <div class="services">
      <h2 class="services-title">SERVICES</h2>
      <p class="services-list">
        Custom Paint &amp; Stain<span class="sep">|</span>Interior &amp; Exterior<span class="sep">|</span>Epoxy Coatings / Garage Floors<br>
        Cabinet Refinishing<span class="sep">|</span>Log Staining and Refinishing.
      </p>
    </div>
  </section>

  <section class="card card-front" aria-label="Card front">
    <div class="faint-mark"></div>
    <div class="brand">
      <span class="brand-mark"></span>
      <span class="brand-name">Venaza Coatings</span>
    </div>
    <div class="accent-bar"></div>
    <div class="holder">
      <h1 class="holder-name">Rodrigo Venaza</h1>
      <p class="holder-title">Director</p>
      <div class="holder-rule"></div>
      <ul class="contact-list">
        <li>
          <svg viewBox="0 0 24 24" aria-hidden="true"><path fill="#1aa3e6" d="M6.6 10.8a15 15 0 0 0 6.6 6.6l2.2-2.2c.3-.3.7-.4 1-.2 1.1.4 2.3.6 3.6.6.6 0 1 .4 1 1V20c0 .6-.4 1-1 1A17 17 0 0 1 3 4c0-.6.4-1 1-1h3.5c.6 0 1 .4 1 1 0 1.3.2 2.5.6 3.6.1.3 0 .7-.2 1z"/></svg>
          801-437-2916
        </li>
        <li>
          <svg viewBox="0 0 24 24" aria-hidden="true"><rect x="2" y="5" width="20" height="14" rx="2" fill="none" stroke="#1aa3e6" stroke-width="2"/><path d="M3 6l9 7 9-7" fill="none" stroke="#1aa3e6" stroke-width="2"/></svg>
          Venazacoatings.utah@brushmail.net
        </li>
        <li>
          <svg viewBox="0 0 24 24" aria-hidden="true"><circle cx="12" cy="12" r="9" fill="none" stroke="#1aa3e6" stroke-width="2"/><path d="M3 12h18M12 3c3 3 3 15 0 18M12 3c-3 3-3 15 0 18" fill="none" stroke="#1aa3e6" stroke-width="1.6"/></svg>
          www.venazacoatings-utah.net
        </li>
      </ul>
    </div>
  </section>

</main>
</body>
</html>
```